A website for a green bio-plastics manufacturing company

We need a home page designed and two complimentary template pages that can be used for the rest of the website. The template page should vary in design from the home page, but should flow uniformly with it.

This is a very innovative company with a proprietary manufacturing method of using bird feathers to make plastic.

The site should be functional, informative, user-friendly and informative to both our business partners and the consumers.
Updates

I've added a more concise overview of the company.  If any of the designers have any questions for me, please ask.  Thanks

Felix

Target Market(s)

Business partners interested in using bio-plastics for their products and general customers.

Industry/Entity Type

Manufacturing

Number of Pages Required

3 pages

Requirements
Must have
• I attached some information about the company, so the site should be designed to incorporate that content.

Will need to be edited by Adobe Contribute.

Easy to navigate

One of the template pages should have one column for content. The other should have two columns. I''m open to different ideas though.

Should be very pleasing to the eye and uncluttered.

Want to be informative to both our business partners as well as consumers who may be researching our product(s)

Easy to Maintain

Anticipated Tabs/Pages
· Home Page
o General “welcome” page

· About Us
o Company overview and information

· Products
o Horticulture Containers
o Agriculture Films
o Where to Buy
o Upcoming Products

· Business Partners

· Press Releases

· Contact Us

Nice to have
• Would like to have earth tones and or nice greens in the color scheme. They make use of bird feathers for their manufacturing process, so perhaps a real sharp image of a feather can be incorporated into the design. Be creative though.

Perhaps a jQuery nav bar, but that may be out of scope.

Should not have
• No flash at all.

```html
<!DOCTYPE html>
<html lang="en">
<head>
<meta charset="utf-8">
<title>Plumeworks Polymers – Website Templates</title>
<link rel="stylesheet" href="https://fonts.googleapis.com/css2?family=PT+Sans+Narrow:wght@400;700&family=Arimo:wght@400;700&display=swap">
<style>
:root{
  --green:#3cad0e;
  --green-dark:#2a8a06;
  --green-deep:#16773a;
  --green-text:#17843a;
  --hero:#c6edb4;
  --hero-light:#e2f7d8;
  --cream:#fbf9ef;
  --text:#5a5a5a;
  --text-dark:#333;
  --grey-line:#d8d8d8;
  --btn:#5d5550;
}
*{margin:0;padding:0;box-sizing:border-box}
html,body{width:1200px;height:3070px;overflow:hidden;background:#fff}
body{font-family:"Arimo",Arial,sans-serif;color:var(--text);position:relative}
.page{position:absolute;left:0;width:1200px}
.page-home{top:0;height:1087px}
.page-menu{top:1144px;height:1087px}
.page-about{top:2278px;height:792px}

.site-header{height:113px;background:linear-gradient(to bottom,#fff,var(--cream));position:relative}
.site-header .inner{width:900px;margin:0 auto;height:100%;position:relative;border-left:1px solid #efeee4;border-right:1px solid #efeee4}
.brand{position:absolute;left:24px;top:30px;display:flex;align-items:center;gap:10px}
.brand-mark{width:56px;height:56px;border-radius:50%;background:var(--green-deep)}
.brand-name{font-family:"PT Sans Narrow",sans-serif;font-weight:400;font-size:30px;color:#2b2b2b;line-height:1}
.contact-line{position:absolute;right:18px;top:77px;font-family:"PT Sans Narrow",sans-serif;font-size:17px;color:#444}
.contact-line b{color:var(--green-text)}

.main-nav{height:50px;background:linear-gradient(to bottom,var(--green-dark) 0,var(--green) 3px,var(--green) 100%);position:relative}
.main-nav .inner{width:900px;margin:0 auto;height:100%;position:relative}
.nav-item{position:absolute;top:0;height:50px;line-height:50px;font-family:"PT Sans Narrow",sans-serif;font-weight:700;font-size:14px;color:#fff;text-transform:uppercase}
.nav-item.has-sub::after{content:"";display:inline-block;margin-left:5px;border:3px solid transparent;border-top:4px solid #bfeaa0;vertical-align:1px}
.nav-item.active{background:var(--green-deep);padding:0 14px;margin-left:-14px}
.search{position:absolute;left:640px;top:13px;width:184px;height:24px;background:#fff;border:1px solid #9fd57f;font-size:10px;color:#888;line-height:22px;padding-left:26px}
.search svg{position:absolute;left:5px;top:4px}
.submit{position:absolute;left:827px;top:13px;width:54px;height:24px;background:#7d7d7d;color:#fff;font-family:"PT Sans Narrow",sans-serif;font-weight:700;font-size:12px;text-align:center;line-height:24px}

.dropdown{position:absolute;left:156px;top:50px;width:147px;background:var(--green-deep);z-index:5;padding:4px 0}
.dropdown a{display:block;height:38px;line-height:38px;padding-left:12px;color:#fff;font-family:"PT Sans Narrow",sans-serif;font-size:13px;text-transform:uppercase;text-decoration:none}

.hero{height:282px;background:linear-gradient(to right,#e6f8de 0,var(--hero) 25%,var(--hero) 75%,#e6f8de 100%)}
.hero .inner{width:900px;margin:0 auto;height:100%;position:relative;background:radial-gradient(circle at 25% 45%,#f4fcf0 0,var(--hero-light) 30%,var(--hero) 70%)}
.hero-feather{position:absolute;left:40px;top:25px;width:300px;height:175px;background:linear-gradient(135deg,#4a2f1c,#8a6a4c 55%,#d9e8cc);border-radius:60% 20% 60% 20%;opacity:.85}
.slogan{position:absolute;left:384px;top:38px;font-family:"PT Sans Narrow",sans-serif;font-size:45px;color:var(--green-text);font-weight:400;line-height:1.1}
.hero p{position:absolute;left:384px;top:99px;width:490px;font-size:11.8px;line-height:15px;color:#333}
.btn-more{position:absolute;left:384px;top:186px;width:157px;height:38px;border-radius:19px;background:linear-gradient(#7a716b,var(--btn));color:#fff;font-family:"PT Sans Narrow",sans-serif;font-weight:700;font-size:17px;text-align:center;line-height:38px;box-shadow:0 1px 2px rgba(0,0,0,.3)}

.features{height:172px;background:linear-gradient(#fff,#f3f3f3);width:900px;margin:0 auto;position:relative;border-bottom:1px dotted #c8c8c8}
.feature{position:absolute;top:28px;width:190px}
.feature h3{font-family:"PT Sans Narrow",sans-serif;font-weight:700;font-size:17px;color:#333;display:flex;align-items:center;gap:4px;white-space:nowrap}
.feature p{margin:4px 0 0 18px;font-size:9.6px;line-height:12.4px;color:#666;width:168px}
.feature .read{position:absolute;left:18px;top:110px;font-family:"PT Sans Narrow",sans-serif;font-weight:700;font-size:12px;color:var(--green);white-space:nowrap}

.welcome{height:422px;width:900px;margin:0 auto;background:#fff;padding:32px 28px 0;box-shadow:0 0 8px rgba(0,0,0,.06)}
.welcome h2,.col-main h2{font-family:"PT Sans Narrow",sans-serif;font-weight:400;font-size:28px;color:#222;margin-bottom:6px}
.welcome h2 b,.col-main h2 b{color:var(--green-text);font-weight:700}
.copy{font-size:11.2px;line-height:16px;color:#666;margin-bottom:16px}
.ticks{list-style:none;margin:34px 0 0 35px}
.ticks li{position:relative;padding-left:22px;font-size:11.2px;line-height:16px;color:#666;margin-bottom:11px}
.ticks li svg{position:absolute;left:0;top:3px}

.site-footer{height:48px;width:900px;margin:0 auto;background:var(--green-deep);color:#fff;font-size:10px;display:flex;justify-content:space-between;align-items:center;padding:0 18px}
.site-footer nav span{margin:0 4px;opacity:.8}

.banner{height:73px;background:linear-gradient(to right,#e6f8de,var(--hero) 30%,var(--hero) 70%,#e6f8de)}
.banner .inner{width:900px;margin:0 auto;height:100%;position:relative}
.banner h1{position:absolute;left:18px;top:10px;font-family:"PT Sans Narrow",sans-serif;font-weight:400;font-size:46px;line-height:1.1;color:var(--green-text)}
.banner-feather{position:absolute;left:708px;top:0;width:168px;height:108px;background:linear-gradient(135deg,#3e2a1a,#8c6d4f 55%,#e3efd8);border-radius:60% 20% 60% 20%;opacity:.85;z-index:2}

.content{height:509px;width:900px;margin:0 auto;position:relative;background:#fff}
.col-main{position:absolute;left:28px;top:32px;width:590px}
.col-main .copy{font-size:11px;line-height:16px}
.col-main .ticks{margin:28px 0 0 35px}
.col-main .ticks li{font-weight:700;color:#555;font-size:11px;margin-bottom:12px}
.side-nav{position:absolute;left:665px;top:72px;width:216px;border-top:1px solid #e2e2e2}
.side-nav a{display:block;height:34px;line-height:34px;padding-left:20px;background:#f1f1f1;border-bottom:1px solid #dcdcdc;font-size:11px;font-weight:700;color:#444;text-decoration:none}
.side-nav a.hover{background:#e4e4e4;color:#aaa;font-weight:400}
.page-about .site-footer{height:47px}
</style>
</head>
<body>

<!-- HOME PAGE -->
<section class="page page-home">
  <header class="site-header"><div class="inner">
    <div class="brand"><span class="brand-mark"></span><span class="brand-name">Plumeworks Polymers</span></div>
    <div class="contact-line">Contact Us Today! <b>(555) 014 2290</b></div>
  </div></header>
  <nav class="main-nav"><div class="inner">
    <span class="nav-item" style="left:17px">Home</span>
    <span class="nav-item has-sub" style="left:84px">About Us</span>
    <span class="nav-item has-sub" style="left:169px">Products</span>
    <span class="nav-item" style="left:260px">Business Partners</span>
    <span class="nav-item" style="left:399px">Press Releases</span>
    <span class="nav-item" style="left:515px">Contact Us</span>
    <div class="search"><svg width="14" height="14" viewBox="0 0 14 14"><circle cx="6" cy="6" r="4.5" fill="none" stroke="#777" stroke-width="1.6"/><line x1="9.3" y1="9.3" x2="13" y2="13" stroke="#777" stroke-width="1.8"/></svg>Search</div>
    <div class="submit">SUBMIT</div>
  </div></nav>
  <div class="hero"><div class="inner">
    <div class="hero-feather" role="img" aria-label="Photograph of a brown bird feather"></div>
    <h2 class="slogan">A good slogan here</h2>
    <p>Lorem ipsum dolor sit amet, consectetur adipiscing elit. Sed nisi neque, pharetra vel vehicula a, molestie quis tortor. Donec ut dui nec neque condimentum adipiscing. Sed pellentesque nisi in tellus congue pellentesque. Etiam a auctor tortor. Curabitur sollicitudin accumsan mauris vel faucibus. Proin accumsan leo at arcu accumsan semper. Phasellus justo lorem, sagittis quis sodales in, porta posuere velit.</p>
    <div class="btn-more">LEARN MORE &nbsp;›</div>
  </div></div>
  <div class="features">
    <div class="feature" style="left:25px"><h3><svg width="14" height="18" viewBox="0 0 14 18"><path d="M2 17 L12 1" stroke="#888" stroke-width="1.5"/></svg>Horticulture Containers</h3><p>Lorem ipsum dolor sit amet, consectetur adipiscing elit. Sed nisi neque, pharetra vel vehicula a, molestie quis tortor. Donec ut dui nec neque condimentum adipiscing.</p><span class="read">› READ MORE</span></div>
    <div class="feature" style="left:242px"><h3><svg width="14" height="18" viewBox="0 0 14 18"><path d="M2 17 L12 1" stroke="#888" stroke-width="1.5"/></svg>Agriculture Films</h3><p>Lorem ipsum dolor sit amet, consectetur adipiscing elit. Sed nisi neque, pharetra vel vehicula a, molestie quis tortor. Donec ut dui nec neque condimentum adipiscing.</p><span class="read">› READ MORE</span></div>
    <div class="feature" style="left:468px"><h3><svg width="14" height="18" viewBox="0 0 14 18"><path d="M2 17 L12 1" stroke="#888" stroke-width="1.5"/></svg>Where to Buy</h3><p>Lorem ipsum dolor sit amet, consectetur adipiscing elit. Sed nisi neque, pharetra vel vehicula a, molestie quis tortor. Donec ut dui nec neque condimentum adipiscing.</p><span class="read">› READ MORE</span></div>
    <div class="feature" style="left:684px"><h3><svg width="14" height="18" viewBox="0 0 14 18"><path d="M2 17 L12 1" stroke="#888" stroke-width="1.5"/></svg>Upcoming Products</h3><p>Lorem ipsum dolor sit amet, consectetur adipiscing elit. Sed nisi neque, pharetra vel vehicula a, molestie quis tortor. Donec ut dui nec neque condimentum adipiscing.</p><span class="read">› READ MORE</span></div>
  </div>
  <main class="welcome">
    <h2>Welcome to <b>Plumeworks Polymers</b></h2>
    <p class="copy">Lorem ipsum dolor sit amet, consectetur adipiscing elit. Sed nisi neque, pharetra vel vehicula a, molestie quis tortor. Donec ut dui nec neque condimentum adipiscing. Sed pellentesque nisi in tellus congue pellentesque. Etiam a auctor tortor. Curabitur sollicitudin accumsan mauris vel faucibus. Proin accumsan leo at arcu accumsan semper. Phasellus justo lorem, sagittis quis sodales in, porta posuere velit. Nulla tellus nibh, auctor sed faucibus vitae, adipiscing at arcu. Cras odio ante, fringilla eu commodo in, elementum eget felis. Mauris nec ante diam. In auctor neque at tellus suscipit et gravida lectus mollis. Mauris dui dui, commodo et tristique eget, condimentum id quam. Nam auctor, urna sed tincidunt dictum, ligula diam bibendum mauris, eu consequat ipsum nibh at mi. Cum sociis natoque penatibus et magnis dis parturient montes, nascetur ridiculus mus. Quisque scelerisque vestibulum enim, in vestibulum mi rhoncus eget. Integer sagittis commodo turpis vel scelerisque. Vestibulum eget sapien at enim tincidunt sollicitudin eget aliquam ante. Proin tortor erat, sodales ut gravida nec, congue quis velit.</p>
    <p class="copy">Fusce quis erat lectus, eu congue risus. In hac habitasse platea dictumst. Nunc dolor erat, vestibulum consectetur tristique in, vestibulum a arcu. Curabitur risus tellus, porttitor quis eleifend sit amet, iaculis sed urna. Cras eget ultricies nisl. Morbi consectetur ipsum id urna consequat consequat. Mauris facilisis porttitor magna, vel varius erat pretium vel.</p>
    <ul class="ticks">
      <li><svg width="11" height="9" viewBox="0 0 11 9"><path d="M1 4.5 L4 7.5 L10 1" fill="none" stroke="#3cad0e" stroke-width="1.6"/></svg>Fusce quis erat lectus, eu congue risus. In hac habitasse platea dictumst. Nunc dolor erat, vestibulum consectetur tristique in, vestibulum a arcu. Curabitur risus tellus, porttitor quis eleifend sit amet, iaculis sed urna.</li>
      <li><svg width="11" height="9" viewBox="0 0 11 9"><path d="M1 4.5 L4 7.5 L10 1" fill="none" stroke="#3cad0e" stroke-width="1.6"/></svg>Duis mauris dui, vestibulum vel cursus vitae, lobortis ac nibh. Duis volutpat scelerisque odio. Suspendisse consequat turpis augue, non ultrices neque.</li>
      <li><svg width="11" height="9" viewBox="0 0 11 9"><path d="M1 4.5 L4 7.5 L10 1" fill="none" stroke="#3cad0e" stroke-width="1.6"/></svg>Curabitur sit amet lectus ut lorem vestibulum interdum euismod dictum lorem. Vivamus venenatis felis in ligula porttitor faucibus. Praesent gravida velit in erat ornare venenatis. Mauris eget urna id tellus imperdiet tincidunt.</li>
    </ul>
  </main>
  <footer class="site-footer"><span>© &nbsp;Copyright &nbsp;2010 Plumeworks Polymers. All rights reserved.</span><nav>Home<span>|</span>About Us<span>|</span>Products<span>|</span>Business Partners<span>|</span>Press Releases<span>|</span>Contact Us</nav></footer>
</section>

<!-- HOME PAGE WITH PRODUCTS MENU OPEN -->
<section class="page page-menu">
  <header class="site-header"><div class="inner">
    <div class="brand"><span class="brand-mark"></span><span class="brand-name">Plumeworks Polymers</span></div>
    <div class="contact-line">Contact Us Today! <b>(555) 014 2290</b></div>
  </div></header>
  <nav class="main-nav"><div class="inner">
    <span class="nav-item" style="left:17px">Home</span>
    <span class="nav-item has-sub" style="left:84px">About Us</span>
    <span class="nav-item has-sub active" style="left:169px">Products</span>
    <span class="nav-item" style="left:260px">Business Partners</span>
    <span class="nav-item" style="left:399px">Press Releases</span>
    <span class="nav-item" style="left:515px">Contact Us</span>
    <div class="search"><svg width="14" height="14" viewBox="0 0 14 14"><circle cx="6" cy="6" r="4.5" fill="none" stroke="#777" stroke-width="1.6"/><line x1="9.3" y1="9.3" x2="13" y2="13" stroke="#777" stroke-width="1.8"/></svg>Search</div>
    <div class="submit">SUBMIT</div>
    <div class="dropdown"><a>Horticulture Containers</a><a>Agriculture Films</a><a>Where to Buy</a><a>Upcoming Products</a></div>
  </div></nav>
  <div class="hero"><div class="inner">
    <div class="hero-feather" role="img" aria-label="Photograph of a brown bird feather"></div>
    <h2 class="slogan">A good slogan here</h2>
    <p>Lorem ipsum dolor sit amet, consectetur adipiscing elit. Sed nisi neque, pharetra vel vehicula a, molestie quis tortor. Donec ut dui nec neque condimentum adipiscing. Sed pellentesque nisi in tellus congue pellentesque. Etiam a auctor tortor. Curabitur sollicitudin accumsan mauris vel faucibus. Proin accumsan leo at arcu accumsan semper. Phasellus justo lorem, sagittis quis sodales in, porta posuere velit.</p>
    <div class="btn-more">LEARN MORE &nbsp;›</div>
  </div></div>
  <div class="features">
    <div class="feature" style="left:25px"><h3><svg width="14" height="18" viewBox="0 0 14 18"><path d="M2 17 L12 1" stroke="#888" stroke-width="1.5"/></svg>Horticulture Containers</h3><p>Lorem ipsum dolor sit amet, consectetur adipiscing elit. Sed nisi neque, pharetra vel vehicula a, molestie quis tortor. Donec ut dui nec neque condimentum adipiscing.</p><span class="read">› READ MORE</span></div>
    <div class="feature" style="left:242px"><h3><svg width="14" height="18" viewBox="0 0 14 18"><path d="M2 17 L12 1" stroke="#888" stroke-width="1.5"/></svg>Agriculture Films</h3><p>Lorem ipsum dolor sit amet, consectetur adipiscing elit. Sed nisi neque, pharetra vel vehicula a, molestie quis tortor. Donec ut dui nec neque condimentum adipiscing.</p><span class="read">› READ MORE</span></div>
    <div class="feature" style="left:468px"><h3><svg width="14" height="18" viewBox="0 0 14 18"><path d="M2 17 L12 1" stroke="#888" stroke-width="1.5"/></svg>Where to Buy</h3><p>Lorem ipsum dolor sit amet, consectetur adipiscing elit. Sed nisi neque, pharetra vel vehicula a, molestie quis tortor. Donec ut dui nec neque condimentum adipiscing.</p><span class="read">› READ MORE</span></div>
    <div class="feature" style="left:684px"><h3><svg width="14" height="18" viewBox="0 0 14 18"><path d="M2 17 L12 1" stroke="#888" stroke-width="1.5"/></svg>Upcoming Products</h3><p>Lorem ipsum dolor sit amet, consectetur adipiscing elit. Sed nisi neque, pharetra vel vehicula a, molestie quis tortor. Donec ut dui nec neque condimentum adipiscing.</p><span class="read">› READ MORE</span></div>
  </div>
  <main class="welcome">
    <h2>Welcome to <b>Plumeworks Polymers</b></h2>
    <p class="copy">Lorem ipsum dolor sit amet, consectetur adipiscing elit. Sed nisi neque, pharetra vel vehicula a, molestie quis tortor. Donec ut dui nec neque condimentum adipiscing. Sed pellentesque nisi in tellus congue pellentesque. Etiam a auctor tortor. Curabitur sollicitudin accumsan mauris vel faucibus. Proin accumsan leo at arcu accumsan semper. Phasellus justo lorem, sagittis quis sodales in, porta posuere velit. Nulla tellus nibh, auctor sed faucibus vitae, adipiscing at arcu. Cras odio ante, fringilla eu commodo in, elementum eget felis. Mauris nec ante diam. In auctor neque at tellus suscipit et gravida lectus mollis. Mauris dui dui, commodo et tristique eget, condimentum id quam. Nam auctor, urna sed tincidunt dictum, ligula diam bibendum mauris, eu consequat ipsum nibh at mi. Cum sociis natoque penatibus et magnis dis parturient montes, nascetur ridiculus mus. Quisque scelerisque vestibulum enim, in vestibulum mi rhoncus eget. Integer sagittis commodo turpis vel scelerisque. Vestibulum eget sapien at enim tincidunt sollicitudin eget aliquam ante. Proin tortor erat, sodales ut gravida nec, congue quis velit.</p>
    <p class="copy">Fusce quis erat lectus, eu congue risus. In hac habitasse platea dictumst. Nunc dolor erat, vestibulum consectetur tristique in, vestibulum a arcu. Curabitur risus tellus, porttitor quis eleifend sit amet, iaculis sed urna. Cras eget ultricies nisl. Morbi consectetur ipsum id urna consequat consequat. Mauris facilisis porttitor magna, vel varius erat pretium vel.</p>
    <ul class="ticks">
      <li><svg width="11" height="9" viewBox="0 0 11 9"><path d="M1 4.5 L4 7.5 L10 1" fill="none" stroke="#3cad0e" stroke-width="1.6"/></svg>Fusce quis erat lectus, eu congue risus. In hac habitasse platea dictumst. Nunc dolor erat, vestibulum consectetur tristique in, vestibulum a arcu. Curabitur risus tellus, porttitor quis eleifend sit amet, iaculis sed urna.</li>
      <li><svg width="11" height="9" viewBox="0 0 11 9"><path d="M1 4.5 L4 7.5 L10 1" fill="none" stroke="#3cad0e" stroke-width="1.6"/></svg>Duis mauris dui, vestibulum vel cursus vitae, lobortis ac nibh. Duis volutpat scelerisque odio. Suspendisse consequat turpis augue, non ultrices neque.</li>
      <li><svg width="11" height="9" viewBox="0 0 11 9"><path d="M1 4.5 L4 7.5 L10 1" fill="none" stroke="#3cad0e" stroke-width="1.6"/></svg>Curabitur sit amet lectus ut lorem vestibulum interdum euismod dictum lorem. Vivamus venenatis felis in ligula porttitor faucibus. Praesent gravida velit in erat ornare venenatis. Mauris eget urna id tellus imperdiet tincidunt.</li>
    </ul>
  </main>
  <footer class="site-footer"><span>© &nbsp;Copyright &nbsp;2010 Plumeworks Polymers. All rights reserved.</span><nav>Home<span>|</span>About Us<span>|</span>Products<span>|</span>Business Partners<span>|</span>Press Releases<span>|</span>Contact Us</nav></footer>
</section>

<!-- ABOUT US TEMPLATE -->
<section class="page page-about">
  <header class="site-header"><div class="inner">
    <div class="brand"><span class="brand-mark"></span><span class="brand-name">Plumeworks Polymers</span></div>
    <div class="contact-line">Contact Us Today! <b>(555) 014 2290</b></div>
  </div></header>
  <nav class="main-nav"><div class="inner">
    <span class="nav-item" style="left:17px">Home</span>
    <span class="nav-item has-sub" style="left:84px">About Us</span>
    <span class="nav-item has-sub" style="left:169px">Products</span>
    <span class="nav-item" style="left:260px">Business Partners</span>
    <span class="nav-item" style="left:399px">Press Releases</span>
    <span class="nav-item" style="left:515px">Contact Us</span>
    <div class="search"><svg width="14" height="14" viewBox="0 0 14 14"><circle cx="6" cy="6" r="4.5" fill="none" stroke="#777" stroke-width="1.6"/><line x1="9.3" y1="9.3" x2="13" y2="13" stroke="#777" stroke-width="1.8"/></svg>Search</div>
    <div class="submit">SUBMIT</div>
  </div></nav>
  <div class="banner"><div class="inner">
    <h1>About Us</h1>
    <div class="banner-feather" role="img" aria-label="Photograph of a brown bird feather"></div>
  </div></div>
  <div class="content">
    <article class="col-main">
      <h2>All about <b>Plumeworks Polymers</b></h2>
      <p class="copy">Lorem ipsum dolor sit amet, consectetur adipiscing elit. Sed nisi neque, pharetra vel vehicula a, molestie quis tortor. Donec ut dui nec neque condimentum adipiscing. Sed pellentesque nisi in tellus congue pellentesque. Etiam a auctor tortor. Curabitur sollicitudin accumsan mauris vel faucibus. Proin accumsan leo at arcu accumsan semper. Phasellus justo lorem, sagittis quis sodales in, porta posuere velit. Nulla tellus nibh, auctor sed faucibus vitae, adipiscing at arcu. Cras odio ante, fringilla eu commodo in, elementum eget felis. Mauris nec ante diam. In auctor neque at tellus suscipit et gravida lectus mollis. Mauris dui dui, commodo et tristique eget, condimentum id quam. Nam auctor, urna sed tincidunt dictum, ligula diam bibendum mauris, eu consequat ipsum nibh at mi. Cum sociis natoque penatibus et magnis dis parturient montes, nascetur ridiculus mus. Quisque scelerisque vestibulum enim, in vestibulum mi rhoncus eget. Integer sagittis commodo turpis vel scelerisque. Vestibulum eget sapien at enim tincidunt sollicitudin eget aliquam ante. Proin tortor erat, sodales ut gravida nec, congue quis velit.</p>
      <p class="copy">Fusce quis erat lectus, eu congue risus. In hac habitasse platea dictumst. Nunc dolor erat, vestibulum consectetur tristique in, vestibulum a arcu. Curabitur risus tellus, porttitor quis eleifend sit amet, iaculis sed urna. Cras eget ultricies nisl. Morbi consectetur ipsum id urna consequat consequat. Mauris facilisis porttitor magna, vel varius erat pretium vel.</p>
      <ul class="ticks">
        <li><svg width="11" height="9" viewBox="0 0 11 9"><path d="M1 4.5 L4 7.5 L10 1" fill="none" stroke="#3cad0e" stroke-width="1.6"/></svg>Fusce quis erat lectus, eu congue risus. In hac habitasse platea dictumst. Nunc dolor erat, vestibulum consectetur tristique in, vestibulum a arcu. Curabitur risus tellus, porttitor quis eleifend sit amet, iaculis sed urna.</li>
        <li><svg width="11" height="9" viewBox="0 0 11 9"><path d="M1 4.5 L4 7.5 L10 1" fill="none" stroke="#3cad0e" stroke-width="1.6"/></svg>Duis mauris dui, vestibulum vel cursus vitae, lobortis ac nibh. Duis volutpat scelerisque odio. Suspendisse consequat turpis augue, non ultrices neque.</li>
        <li><svg width="11" height="9" viewBox="0 0 11 9"><path d="M1 4.5 L4 7.5 L10 1" fill="none" stroke="#3cad0e" stroke-width="1.6"/></svg>Curabitur sit amet lectus ut lorem vestibulum interdum euismod dictum lorem. Vivamus venenatis felis in ligula porttitor faucibus. Praesent gravida velit in erat ornare venenatis. Mauris eget urna id tellus imperdiet tincidunt.</li>
      </ul>
    </article>
    <aside class="side-nav">
      <a>Company Description</a>
      <a class="hover">Vision &amp; Statement</a>
      <a>Vision &amp; Statement</a>
      <a>Core Values &amp; Beliefs</a>
      <a>Business Goals</a>
    </aside>
  </div>
  <footer class="site-footer"><span>© &nbsp;Copyright &nbsp;2010 Plumeworks Polymers. All rights reserved.</span><nav>Home<span>|</span>About Us<span>|</span>Products<span>|</span>Business Partners<span>|</span>Press Releases<span>|</span>Contact Us</nav></footer>
</section>

</body>
</html>
```